Varnoly Waste Website Design

Our new start-up needs a website design. We plan to help businesses find more sustainable ways to manage their waste. Our initial website aims to gather contact data from potential business customers and comprehensive information from waste facilities and waste transporters. We have a logo design (attached) which we would like included in the website design. I have also attached a number of pages that describe what information should appear on each page as well as a web design brief file that describes the look we are after.

```html
<!DOCTYPE html>
<html lang="en">
<head>
<meta charset="utf-8">
<title>Varnoly Waste</title>
<link href="https://fonts.googleapis.com/css2?family=Jost:wght@300;400;500;600&display=swap" rel="stylesheet">
<style>
:root{
  --green:#74b62e;
  --green-light:#a6cf35;
  --green-dark:#5d9d2a;
  --ink:#333333;
  --muted:#555a60;
  --rule:#cfd2d8;
  --footer-bg:#f4f5f9;
  --white:#ffffff;
}
*{margin:0;padding:0;box-sizing:border-box}
html,body{width:1200px;height:904px;overflow:hidden;background:var(--white)}
body{font-family:'Jost',sans-serif;color:var(--ink);position:relative}
a{text-decoration:none;color:inherit}

.site-header{position:absolute;left:0;top:0;width:1200px;height:80px;background:var(--white)}
.brand{position:absolute;left:156px;top:22px;display:flex;align-items:center;gap:10px}
.brand-dot{width:36px;height:36px;border-radius:50%;border:3px solid var(--green)}
.brand-name{font-size:22px;font-weight:500;color:var(--muted);letter-spacing:1px;white-space:nowrap}
.main-nav{position:absolute;top:33px;left:0;font-size:12px;font-weight:400;letter-spacing:1.8px;text-transform:uppercase}
.main-nav a{position:absolute;white-space:nowrap;color:var(--ink)}
.nav-home{left:415px;top:-1px}
.header-phone{position:absolute;left:912px;top:28px;display:flex;align-items:center;gap:8px;font-size:17px;letter-spacing:1px;color:var(--ink);white-space:nowrap}

.hero{position:absolute;left:0;top:80px;width:1200px;height:455px;
  background:linear-gradient(100deg,#4a5a3e 0%,#7a6a2c 25%,#8a6b24 42%,#4e5a3a 68%,#34422e 100%)}
.hero::after{content:"";position:absolute;inset:0;background:rgba(0,0,0,.35)}
.hero-content{position:absolute;left:0;top:0;width:100%;z-index:1;text-align:center;color:var(--white)}
.hero-kicker{position:absolute;top:130px;width:100%;font-size:27px;font-weight:300;letter-spacing:1px}
.hero-kicker strong{color:var(--green-light);font-weight:500}
.hero-title{position:absolute;top:170px;width:100%;font-size:47px;font-weight:300;letter-spacing:1.5px}
.hero-actions{position:absolute;top:252px;left:0;width:100%;height:41px}
.btn{position:absolute;height:41px;border:2px solid var(--white);border-radius:21px;
  font-size:11.5px;font-weight:500;letter-spacing:1.8px;text-transform:uppercase;color:var(--white);
  display:flex;align-items:center;justify-content:center;white-space:nowrap}
.btn-producers{left:308px;width:208px}
.btn-facilities{left:524px;width:192px;background:var(--white);color:var(--green-dark)}
.btn-transporters{left:724px;width:192px}

.site-footer{position:absolute;left:0;top:535px;width:1200px;height:369px;background:var(--footer-bg)}
.footer-mark{position:absolute;left:573px;top:50px;width:54px;height:54px;border-radius:50%;border:3px solid var(--green)}
.footer-contact{position:absolute;top:141px;width:100%;text-align:center;font-size:16px;color:var(--ink);letter-spacing:.5px}
.footer-contact .label{color:var(--green)}
.footer-contact svg{vertical-align:-2px;margin:0 4px}
.footer-nav{position:absolute;left:232px;top:187px;width:735px;height:34px;border-top:1px solid var(--rule);border-bottom:1px solid var(--rule);
  display:flex;justify-content:center;align-items:center;gap:28px;font-size:12px;letter-spacing:1.8px;text-transform:uppercase;color:var(--muted)}
.to-top{position:absolute;left:1068px;top:192px;width:24px;height:24px;border-radius:50%;background:var(--green);display:flex;align-items:center;justify-content:center}
.social{position:absolute;top:252px;left:0;width:100%}
.social span{position:absolute;width:32px;height:32px;border-radius:50%;border:1px solid var(--green)}
.social .active{background:var(--green)}
.copyright{position:absolute;top:315px;width:100%;text-align:center;font-size:12px;color:var(--muted);letter-spacing:.3px}
.copyright .brand-first{color:var(--green);font-weight:600}
.copyright .brand-last{color:var(--ink);font-weight:600}
</style>
</head>
<body>
<header class="site-header">
  <div class="brand"><span class="brand-dot"></span><span class="brand-name">VARNOLY WASTE</span></div>
  <nav class="main-nav">
    <a class="nav-home" href="#"><svg width="12" height="12" viewBox="0 0 12 12"><path d="M6 1 L11 6 H9.5 V11 H7 V8 H5 V11 H2.5 V6 H1 Z" fill="#74b62e"/></svg></a>
    <a href="#" style="left:452px">About Us</a>
    <a href="#" style="left:548px">What We Do</a>
    <a href="#" style="left:666px">Resources</a>
    <a href="#" style="left:773px">Contact Us</a>
  </nav>
  <div class="header-phone">
    <svg width="14" height="14" viewBox="0 0 24 24"><path d="M6.6 10.8a15 15 0 0 0 6.6 6.6l2.2-2.2a1 1 0 0 1 1-.25 11.4 11.4 0 0 0 3.6.57 1 1 0 0 1 1 1V20a1 1 0 0 1-1 1A17 17 0 0 1 3 4a1 1 0 0 1 1-1h3.5a1 1 0 0 1 1 1c0 1.25.2 2.45.57 3.57a1 1 0 0 1-.25 1z" fill="none" stroke="#74b62e" stroke-width="2"/></svg>
    123-456-7890
  </div>
</header>

<section class="hero" role="img" aria-label="Photo of a yellow refuse collection truck lifting a metal waste bin on a tree-lined street">
  <div class="hero-content">
    <p class="hero-kicker">WELCOME TO <strong>VARNOLY WASTE</strong></p>
    <h1 class="hero-title">Take Control of Your Waste Here</h1>
    <div class="hero-actions">
      <a class="btn btn-producers" href="#">Waste Producers</a>
      <a class="btn btn-facilities" href="#">Waste Facilities</a>
      <a class="btn btn-transporters" href="#">Waste Transporters</a>
    </div>
  </div>
</section>

<footer class="site-footer">
  <div class="footer-mark"></div>
  <p class="footer-contact"><span class="label">Call Us:</span><svg width="15" height="15" viewBox="0 0 24 24"><path d="M6.6 10.8a15 15 0 0 0 6.6 6.6l2.2-2.2a1 1 0 0 1 1-.25 11.4 11.4 0 0 0 3.6.57 1 1 0 0 1 1 1V20a1 1 0 0 1-1 1A17 17 0 0 1 3 4a1 1 0 0 1 1-1h3.5a1 1 0 0 1 1 1c0 1.25.2 2.45.57 3.57a1 1 0 0 1-.25 1z" fill="none" stroke="#74b62e" stroke-width="2"/></svg>123-456-7890, &nbsp;<span class="label">E.</span> info@varnolywaste.com</p>
  <nav class="footer-nav">
    <span>About Us</span><span>What We Do</span><span>Resources</span><span>Results</span><span>Final Results</span><span>Contact Us</span>
  </nav>
  <a class="to-top" href="#"><svg width="10" height="8" viewBox="0 0 10 8"><path d="M1 6 L5 2 L9 6 Z" fill="#fff"/></svg></a>
  <div class="social">
    <span style="left:524px"></span>
    <span class="active" style="left:564px"></span>
    <span style="left:603px"></span>
    <span style="left:643px"></span>
  </div>
  <p class="copyright">© 2018 <span class="brand-first">VARNOLY</span> <span class="brand-last">WASTE.</span> All Right Reserved</p>
</footer>
</body>
</html>
```